Compelling Home Page for Clip Reach Forge

We are a Video SEO specialist that get websites on top of the front page of Searvo and ClipTube with video thumbprints that generate great traffic. Video SEO is all we do

see what we're offering at a salespage www.bringmoreclipviews.example. However, please omit "guarantee"

he home page should introduce our company as a premier company for helping brands get their videos on the front page of searvo and high up in cliptube. Should incorporate video "thumbnails" as part of the design. These could be the "triangular click buttons" or little video screens you see as "thumbnails" Needs a prominent place for a video about videoSEO. on Left side of page towards the top.

Needs buttons across the top for other pages. See www.toprankclips.example for frame of reference we want to be better than them.

Must incorporate our logo. We'd like to see the logo on dark background as well as white background.

Simple but with bright and vibrant highlights that look sophisticated, cutting edge and accountable. Shows credentials. Links with examples of thumbnails that are on the front page

We want to beat www.toprankclips.example check it out for point of reference

Target Market(s)

large corporations who have videos already and want to get better traction. Summit 1000. Advertising Agencies for Summit 1000's

Requirements
Must have
• Incorporate our logo. clean, easy to read

```html
<!DOCTYPE html>
<html lang="en">
<head>
<meta charset="utf-8">
<title>Clip Reach Forge – Home</title>
<link href="https://fonts.googleapis.com/css2?family=Arimo:wght@400;700&family=Roboto+Condensed:wght@700&display=swap" rel="stylesheet">
<style>
:root{
  --blue:#0f58e0;
  --blue-dark:#0a3fb8;
  --blue-light:#2f8cf5;
  --nav-active:#1a86f0;
  --gold:#f8c300;
  --text:#333;
  --heading:#555;
  --link:#1a5fd6;
  --orange:#e9530f;
  --panel-title:#17307a;
  --rule:#e2e2e2;
}
*{box-sizing:border-box;margin:0;padding:0}
html,body{width:1200px;height:1055px;overflow:hidden;background:#fff;font-family:Arimo,Arial,sans-serif;color:var(--text)}
.page{position:relative;width:1200px;height:1055px}

.header{position:absolute;top:0;left:0;width:1200px;height:125px;background:linear-gradient(#fff,#f2f2f2 60%,#dcdcdc)}
.brand{position:absolute;left:37px;top:21px;width:387px;height:87px;border-radius:10px;background:linear-gradient(#2b2b2b,#050505);box-shadow:3px 4px 6px rgba(0,0,0,.35);display:flex;align-items:center;padding-left:24px;gap:14px}
.brand-mark{width:46px;height:46px;border-radius:50%;background:var(--blue-light)}
.brand-name{color:#fff;font-size:30px;font-weight:700;letter-spacing:-.5px}
.nav{position:absolute;top:40px;left:654px;height:48px;font-size:15px;color:#222}
.nav a{position:absolute;top:0;height:48px;line-height:48px;color:#222;text-decoration:none;white-space:nowrap}
.nav a.active{left:0;width:83px;text-align:center;color:#fff;border-radius:7px;background:linear-gradient(#38a6ff,var(--nav-active) 50%,#0a66d8)}

.banner{position:absolute;top:125px;left:0;width:1200px;height:289px;background:radial-gradient(ellipse at 75% 40%,#3a8cf6,var(--blue) 55%,var(--blue-dark));box-shadow:0 4px 6px rgba(0,0,0,.25)}
.listings{position:absolute;left:39px;top:14px;width:463px;height:225px;border-radius:9px;background:linear-gradient(#fff,#f4f4f4 55%,#d4d4d4);border:1px solid #bbb}
.listings-reflection{position:absolute;left:39px;top:242px;width:463px;height:40px;border-radius:9px 9px 0 0;background:linear-gradient(rgba(255,255,255,.35),rgba(255,255,255,0))}
.listings h2{position:absolute;left:24px;top:14px;font-size:28px;font-weight:400;color:var(--panel-title)}
.thumbs{position:absolute;left:24px;top:70px;display:flex;gap:8px}
.thumb{width:98px;height:75px;border:2px solid #111;background:linear-gradient(135deg,#2a1a30,#5a3a48 50%,#b07a3a);position:relative}
.thumb .play{position:absolute;right:6px;bottom:6px;width:22px;height:22px;background:#ccc;border-radius:3px}
.thumb .play svg{display:block}
.arrow{position:absolute;top:98px}
.arrow.prev{left:-6px}.arrow.next{right:-6px}
.btn{position:absolute;top:166px;width:95px;height:31px;border-radius:8px;background:linear-gradient(#ff7a2e,var(--orange));color:#fff;font-size:14px;line-height:31px;text-align:center;box-shadow:0 1px 2px rgba(0,0,0,.3)}
.btn.prev-btn{left:24px}.btn.next-btn{left:127px}

.search-art{position:absolute;left:624px;top:40px;width:132px;height:130px;border-radius:50%;background:radial-gradient(circle at 45% 40%,#cfe6ff,#6b8fb8 45%,rgba(40,80,160,0) 72%)}
.headline{position:absolute;right:40px;top:18px;text-align:right;font-family:"Roboto Condensed","Arial Narrow",sans-serif;font-weight:700;font-size:35px;line-height:42px;color:#fff;text-shadow:1px 2px 2px rgba(0,0,0,.35)}
.headline em{font-style:normal;color:var(--gold)}
.tagline{position:absolute;right:42px;top:240px;text-align:right;font-size:14px;line-height:16px;color:#fff}

.top-rule{position:absolute;left:39px;top:435px;width:1119px;height:2px;background:var(--rule)}
.main{position:absolute;left:40px;top:456px;width:778px}
.main h1{font-size:26px;font-weight:400;color:var(--heading);margin-bottom:6px}
.main p{font-size:14px;line-height:23.4px;margin-bottom:23.4px}
.col-rule{position:absolute;left:845px;top:445px;width:4px;height:557px;background:#ececec}

.side-box{position:absolute;left:870px;width:288px;border:1px solid #ddd;border-radius:10px;box-shadow:0 0 5px rgba(0,0,0,.15);background:#fff}
.side-box h3{height:76px;padding:22px 0 0 17px;font-size:26px;font-weight:400;color:#444;border-bottom:3px solid #eee;position:relative}
.side-icon{position:absolute;right:10px;top:14px;width:52px;height:52px}
.blog{top:455px;height:307px}
.testi{top:783px;height:213px}
.entry{padding:16px 12px 0 22px;font-size:13px}
.entry .title{color:var(--link);font-size:14px}
.entry .title::before,.quote::before{content:"»";color:#999;margin-right:8px}
.entry p{margin:10px 0 0 20px;line-height:16px;color:#222}
.meta{margin:14px 0 0 20px;color:var(--link);display:flex;align-items:center;gap:6px}
.quote{padding:17px 0 0 24px;font-size:13px;color:#222}
.quote .who{display:block;text-align:right;padding-right:90px;font-style:italic;margin-top:6px}
.more{position:absolute;right:14px;bottom:10px;font-size:13px;color:var(--link)}

.footer{position:absolute;left:0;top:1017px;width:1200px;height:38px;background:linear-gradient(var(--blue-light),var(--blue));border-top:3px solid #ddd;color:#fff;font-size:13px;text-align:center;line-height:34px}
</style>
</head>
<body>
<div class="page">
  <header class="header">
    <div class="brand"><span class="brand-mark"></span><span class="brand-name">Clip Reach Forge</span></div>
    <nav class="nav">
      <a class="active" href="#">Home</a>
      <a href="#" style="left:96px">About Us</a>
      <a href="#" style="left:190px">Services</a>
      <a href="#" style="left:266px">Blog</a>
      <a href="#" style="left:330px">Portfolio</a>
      <a href="#" style="left:418px">Contact Us</a>
    </nav>
  </header>

  <section class="banner">
    <div class="listings">
      <h2>Video Listings</h2>
      <svg class="arrow prev" width="16" height="18" viewBox="0 0 16 18"><path d="M12 2 4 9l8 7" fill="none" stroke="#111" stroke-width="3.5"/></svg>
      <div class="thumbs">
        <div class="thumb" role="img" aria-label="Video thumbnail"><span class="play"><svg width="22" height="22"><path d="M8 6v10l8-5z" fill="#1d2fa8"/></svg></span></div>
        <div class="thumb" role="img" aria-label="Video thumbnail"><span class="play"><svg width="22" height="22"><path d="M8 6v10l8-5z" fill="#1d2fa8"/></svg></span></div>
        <div class="thumb" role="img" aria-label="Video thumbnail"><span class="play"><svg width="22" height="22"><path d="M8 6v10l8-5z" fill="#1d2fa8"/></svg></span></div>
        <div class="thumb" role="img" aria-label="Video thumbnail"><span class="play"><svg width="22" height="22"><path d="M8 6v10l8-5z" fill="#1d2fa8"/></svg></span></div>
      </div>
      <svg class="arrow next" width="16" height="18" viewBox="0 0 16 18"><path d="M4 2l8 7-8 7" fill="none" stroke="#111" stroke-width="3.5"/></svg>
      <span class="btn prev-btn">‹&nbsp;&nbsp;&nbsp;Prev</span>
      <span class="btn next-btn">Next&nbsp;&nbsp;&nbsp;›</span>
    </div>
    <div class="listings-reflection"></div>
    <div class="search-art" role="img" aria-label="Magnifying glass illustration"></div>
    <div class="headline">"FIRST PAGE <em>VIDEO LISTINGS</em><br>on Searvo for the Keywords<br>of Your Choice...For More<br><em>Traffic</em>, Leads, and Sales to<br>Your Site!"</div>
    <p class="tagline">No matter what you sell or what your company size, VIDEO MARKETING is<br>very likely your best opportunity to &nbsp;dramatically increase online sales this year:</p>
  </section>

  <div class="top-rule"></div>
  <main class="main">
    <h1>Welcome to Clip Reach Forge</h1>
    <p>Lorem Ipsum is simply dummy text of the printing and typesetting industry. Lorem Ipsum has been the industry's standard dummy text ever since the 1500s, when an unknown printer took a galley of type and scrambled it to make a type specimen book. It has survived not only five centuries, but also the leap into electronic typesetting, remaining essentially unchanged. It was popularised in the 1960s with the release of Transfex sheets containing Lorem Ipsum passages, and more recently with desktop publishing software like Quorra PageSmith including versions of Lorem Ipsum.</p>
    <p>Lorem Ipsum is simply dummy text of the printing and typesetting industry. Lorem Ipsum has been the industry's standard dummy text ever since the 1500s, when an unknown printer took a galley of type and scrambled it to make a type specimen book. It has survived not only five centuries, but also the leap into electronic typesetting, remaining essentially unchanged. It was popularised in the 1960s with the release of Transfex sheets containing Lorem Ipsum passages, and more recently with desktop publishing software like Quorra PageSmith including versions of Lorem Ipsum.</p>
  </main>
  <div class="col-rule"></div>

  <aside class="side-box blog">
    <h3>Recent Blog item
      <svg class="side-icon" viewBox="0 0 52 52"><ellipse cx="26" cy="24" rx="23" ry="20" fill="#5ec3f0" stroke="#2a8fc8" stroke-width="2"/><path d="M14 40l-4 9 12-6z" fill="#5ec3f0"/><path d="M14 18h24M14 25h24M14 32h18" stroke="#1f6fa8" stroke-width="2.5"/></svg>
    </h3>
    <div class="entry">
      <span class="title">Why Lorem ipsum dolor?</span>
      <p>Lorem Ipsum is simply dummy text of the printing and typesetting industry.</p>
      <div class="meta"><svg width="14" height="12"><path d="M1 1h12v7H6l-3 3V8H1z" fill="none" stroke="#888"/></svg>Comments 0 &nbsp;<span style="color:#333">|</span>&nbsp; Read More</div>
    </div>
    <div class="entry">
      <span class="title">Why Lorem ipsum dolor?</span>
      <p>Lorem Ipsum is simply dummy text of the printing and typesetting industry.</p>
      <div class="meta"><svg width="14" height="12"><path d="M1 1h12v7H6l-3 3V8H1z" fill="none" stroke="#888"/></svg>Comments 0 &nbsp;<span style="color:#333">|</span>&nbsp; Read More</div>
    </div>
  </aside>

  <aside class="side-box testi">
    <h3>Testimonials
      <span class="side-icon" role="img" aria-label="Note paper with pencil illustration" style="background:linear-gradient(#fafafa,#ddd);border:1px solid #ccc;width:56px;height:56px;top:10px"></span>
    </h3>
    <p class="quote">Good Work - lorem ipsum / 1<span class="who">Marlo Dentra</span></p>
    <p class="quote">Good Work - lorem ipsum / 1<span class="who">Marlo Dentra</span></p>
    <span class="more">Read More</span>
  </aside>

  <footer class="footer">© 2011 Copyright : All Rights Reserved by Clip Reach Forge</footer>
</div>
</body>
</html>
```